Business Card Design

I am a Building Surveyor and run my own Building Consultat company, providing professional advice and services to builders, architects, designers, owners, etc.

Industry/Entity Type

Business

Contact Information for Business Card

Dorwen Halket BBldgSurv (Hons)
Managing Director

57 Quillon Rise, Marrick Heights WA 6148
Mobile 0438 271 594
Email Dorwen.halket@tarnwellpq.com

Requirements
Must have
• I would like the back of the business card to be one colour (a shade of either black or maroon, matching the colours of my logo). Positioned in the centre on the back of the business card is to be my logo.

The front of the card is to be white, with my contact information in either black or maroon. The ADBldgSurv after my name should be in a smaller font size than my name. I would also like a small logo somewhere on this side of the card.

```html
<!DOCTYPE html>
<html lang="en">
<head>
<meta charset="utf-8">
<title>Tarnwell Building Consultants – Business Card</title>
<link href="https://fonts.googleapis.com/css2?family=Alegreya+Sans:wght@400;500;700&display=swap" rel="stylesheet">
<style>
  :root {
    --maroon: #6b1c16;
    --charcoal: #4a4a4c;
    --text-grey: #4d4d4f;
    --card-white: #ffffff;
    --back-black: #2a2a2c;
    --back-text: #e6e6e7;
    --stage-light: #ffffff;
    --stage-edge: #dbe3e6;
  }
  * { margin: 0; padding: 0; box-sizing: border-box; }
  html, body { width: 1200px; height: 1000px; overflow: hidden; }
  body {
    position: relative;
    font-family: "Alegreya Sans", "Helvetica Neue", Arial, sans-serif;
    background: radial-gradient(ellipse 60% 55% at 50% 50%, var(--stage-light) 0%, #f3f6f7 50%, var(--stage-edge) 100%);
  }
  .card {
    position: absolute;
    left: 313px;
    width: 586px;
    height: 361px;
    box-shadow: 0 2px 6px rgba(0,0,0,0.28);
  }
  .card--back {
    top: 82px;
    background: var(--back-black);
  }
  .card--front {
    top: 547px;
    background: var(--card-white);
  }
  .brand {
    position: absolute;
    display: flex;
    align-items: center;
    gap: 12px;
    left: 50%;
    transform: translateX(-50%);
    white-space: nowrap;
  }
  .brand__dot {
    flex: none;
    border-radius: 50%;
    border: 3px solid var(--maroon);
  }
  .brand__name {
    font-weight: 500;
    letter-spacing: 0.04em;
  }
  .card--back .brand { top: 146px; }
  .card--back .brand__dot { width: 62px; height: 62px; }
  .card--back .brand__name { font-size: 21px; color: var(--back-text); }
  .card--front .brand { top: 44px; }
  .card--front .brand__dot { width: 46px; height: 46px; border-width: 2px; }
  .card--front .brand__name { font-size: 15px; color: var(--charcoal); }
  .holder {
    position: absolute;
    top: 175px;
    width: 100%;
    text-align: center;
  }
  .holder__name {
    color: var(--maroon);
    font-weight: 700;
    font-size: 26px;
    line-height: 1.1;
  }
  .holder__credential {
    color: var(--text-grey);
    font-size: 19px;
    line-height: 1.15;
  }
  .contact {
    position: absolute;
    top: 298px;
    width: 100%;
    text-align: center;
    color: var(--text-grey);
    font-size: 18.5px;
    line-height: 22px;
  }
</style>
</head>
<body>
  <section class="card card--back" aria-label="Card back">
    <div class="brand">
      <span class="brand__dot"></span>
      <span class="brand__name">TARNWELL BUILDING CONSULTANTS</span>
    </div>
  </section>

  <section class="card card--front" aria-label="Card front">
    <div class="brand">
      <span class="brand__dot"></span>
      <span class="brand__name">TARNWELL BUILDING CONSULTANTS</span>
    </div>
    <div class="holder">
      <p class="holder__name">Dorwen Halket</p>
      <p class="holder__credential">BBldgSurv (Hons)</p>
    </div>
    <div class="contact">
      <p>Managing Director 57 Quillon Rise, Marrick Heights WA 6148</p>
      <p>Mobile: 0438 271 594 • Email: Dorwen.halket@tarnwellpq.com</p>
    </div>
  </section>
</body>
</html>
```